Zielgruppe
Online Shop Westernartikel
Aufgabenstellung
Wir verkaufen über unseren Online Shop ( www.sattelwind-domizil-laden.de ) Westernbekleidung und Westernreitzubehör ( Buckaroo / Vaquero orientiert ).
Wir beziehen einen großen Teil der Ware aus den Staaten. Ich benötige einen Banner der den Alten ersetzt. Ein neues Logo wurde gestaltet, ist aber noch nicht freigegeben.
Wird das Logo benötigt so kann ich dieses unter Vorbehalt zur Verfügung stellen.
Könnte für das Logo ein Platzhalter vorgesehen werden?
Derzeitige Bannergröße ist 978 x 269

```html
<!DOCTYPE html>
<html lang="de">
<head>
<meta charset="utf-8">
<title>Sattelwind Laden – Banner</title>
<link rel="stylesheet" href="https://fonts.googleapis.com/css2?family=Caveat+Brush&family=Montserrat:wght@800&display=swap">
<style>
  :root {
    --sky-pink: #cf5f88;
    --sky-rose: #d98aa3;
    --mist-blue: #8fa3b6;
    --slate-blue: #5d7f93;
    --deep-teal: #1f3b47;
    --paper-white: #ffffff;
    --brand-berry: #ac4a76;
    --shadow-grey: #d9d9d9;
    --headline-white: #ffffff;
  }
  html, body {
    margin: 0;
    padding: 0;
    overflow: hidden;
    background: var(--paper-white);
  }
  .banner {
    position: relative;
    width: 1200px;
    height: 330px;
    overflow: hidden;
    background: var(--paper-white);
  }
  .banner__scene {
    position: absolute;
    inset: 0;
    background:
      radial-gradient(ellipse 170px 120px at 610px 95px, rgba(250, 214, 190, 0.85), rgba(250, 214, 190, 0) 70%),
      linear-gradient(180deg, var(--sky-pink) 0%, var(--sky-rose) 25%, var(--mist-blue) 48%, var(--slate-blue) 72%, var(--deep-teal) 100%);
  }
  .banner__wedge {
    position: absolute;
    inset: 0;
    width: 1200px;
    height: 330px;
  }
  .banner__wedge polygon {
    fill: var(--paper-white);
  }
  .logo-slot {
    position: absolute;
    left: 43px;
    top: 84px;
    width: 339px;
    height: 145px;
    background: var(--brand-berry);
    box-shadow: 11px 11px 0 var(--shadow-grey);
    display: flex;
    align-items: center;
  }
  .logo-slot__label {
    margin-left: 52px;
    font-family: "Montserrat", sans-serif;
    font-weight: 800;
    font-size: 78px;
    letter-spacing: 1px;
    line-height: 1;
    color: var(--paper-white);
  }
  .headline {
    position: absolute;
    left: 660px;
    top: 112px;
    width: 380px;
    margin: 0;
    text-align: center;
    font-family: "Caveat Brush", cursive;
    font-weight: 400;
    color: var(--headline-white);
    line-height: 1;
  }
  .headline__line {
    display: block;
    font-size: 44px;
    letter-spacing: 1px;
  }
  .headline__line--intro {
    margin-bottom: 4px;
    padding-left: 30px;
  }
  .headline__line--key {
    font-size: 90px;
    margin-top: 2px;
    padding-left: 80px;
  }
</style>
</head>
<body>
  <div class="banner">
    <div class="banner__scene" role="img" aria-label="Illustration: Pferdesilhouette auf einem Hügel vor gestaffelten Bergen, Abendsonne und pinkem Himmel auf Holzstruktur"></div>
    <svg class="banner__wedge" viewBox="0 0 1200 330" aria-hidden="true">
      <polygon points="0,0 357,0 650,160 355,330 0,330"/>
    </svg>
    <div class="logo-slot">
      <span class="logo-slot__label">LOGO</span>
    </div>
    <h1 class="headline">
      <span class="headline__line headline__line--intro">Hier steht</span>
      <span class="headline__line">die gewünschte</span>
      <span class="headline__line headline__line--key">Headline!</span>
    </h1>
  </div>
</body>
</html>
```